Improved Business Card, Government Contracting

We are looking to update the design of our business cards. We would like to create a template that can be used for future employees and easy to update.

Halvorsen Advisory Partners, LLC is a Service Disabled Veteran Owned Small Business with headquarters located in Leavenworth, KS. Our current website is www.hapteam.com. We have contracts in KS and VA with expansion opportunities in various other states. Our primary line of work is within government contracting and providing consulting services to various organizations within the Bureau of Frontier Works. We would like to project a professional image of our company that is consistent with the industry. Provided are previous versions of our business card template that shows our logo as well. We would like to make sure the information on the cards are easily noticeable .

Target Market(s)

Government Officials
Fellow Small Business Contractors
Large Business Contractors (ex. TRUX, Keswell Barnaby, Pryde Okonjo Whitcombe)

Industry/Entity Type

Business

Contact Information for Business Card

Dale Fenwick
Office Manager
Halvorsen Advisory Partners
Ph: 913.555.0172
Email: d.fenwick@hapteam.us
www.hapteam.com

Requirements
Must have
• The business mailing address is:
• 31842 204th Lane
• Leavenworth, KS 66099
Nice to have
• Embossed lettering

```html
<!DOCTYPE html>
<html lang="en">
<head>
<meta charset="utf-8">
<title>Halvorsen Advisory Partners – Business Card</title>
<link rel="stylesheet" href="https://fonts.googleapis.com/css2?family=Open+Sans:wght@400;700&display=swap">
<style>
  :root {
    --stage: #2d2c2d;
    --yellow: #fff10a;
    --blue: #3f5ca3;
    --name-blue: #3a55a0;
    --white: #ffffff;
    --ink: #1f1f1f;
  }
  * { box-sizing: border-box; margin: 0; padding: 0; }
  html, body { width: 961px; height: 1200px; overflow: hidden; }
  body {
    position: relative;
    background: var(--stage);
    font-family: "Open Sans", Arial, sans-serif;
  }
  .side-label {
    position: absolute;
    left: 33px;
    color: var(--white);
    font: 700 31px/1 Arial, "Open Sans", sans-serif;
    letter-spacing: 1px;
    transform: translate(-50%, -50%) rotate(-90deg);
    white-space: nowrap;
  }
  .side-label--front { top: 322px; }
  .side-label--back { top: 872px; }

  .card {
    position: absolute;
    left: 73px;
    width: 815px;
    overflow: hidden;
  }
  .card--front {
    top: 85px;
    height: 478px;
    background: var(--yellow);
  }
  .front-wordmark {
    position: absolute;
    left: 0; right: 0;
    top: 210px;
    text-align: center;
    color: var(--blue);
    font-weight: 400;
    font-size: 40px;
    line-height: 1.15;
  }

  .card--back {
    top: 636px;
    height: 477px;
    background: var(--white);
  }
  .back-wordmark {
    position: absolute;
    left: 58px;
    top: 90px;
    color: var(--blue);
    font-weight: 400;
    font-size: 28px;
    line-height: 1.2;
  }
  .holder {
    position: absolute;
    right: 61px;
    top: 86px;
    text-align: right;
  }
  .holder-name {
    color: var(--name-blue);
    font-size: 34px;
    line-height: 1.1;
  }
  .holder-title {
    color: var(--ink);
    font-size: 18px;
    margin-top: 2px;
  }
  .company-band {
    position: absolute;
    left: 0; top: 246px;
    width: 100%;
    height: 64px;
    background: var(--yellow);
    padding-left: 62px;
    color: var(--blue);
    font-weight: 700;
    font-size: 31px;
    line-height: 64px;
  }
  .contact-panel {
    position: absolute;
    left: 0; top: 310px;
    width: 100%;
    height: 167px;
    background: var(--blue);
    color: var(--white);
    font-size: 22px;
  }
  .contact-row {
    position: absolute;
    left: 0; right: 0;
    display: flex;
    justify-content: center;
    align-items: center;
    gap: 26px;
  }
  .contact-row--lines { top: 44px; }
  .contact-row--address { top: 95px; }
  .contact-item { display: flex; align-items: center; gap: 7px; }
  .contact-item svg { fill: var(--white); flex: none; }
</style>
</head>
<body>
  <div class="side-label side-label--front">SIDE 1</div>
  <div class="side-label side-label--back">SIDE 2</div>

  <section class="card card--front">
    <div class="front-wordmark">Halvorsen<br>Advisory Partners</div>
  </section>

  <section class="card card--back">
    <div class="back-wordmark">Halvorsen<br>Advisory Partners</div>
    <div class="holder">
      <div class="holder-name">Dale Fenwick</div>
      <div class="holder-title">Office Manager</div>
    </div>
    <div class="company-band">Halvorsen Advisory Partners</div>
    <div class="contact-panel">
      <div class="contact-row contact-row--lines">
        <span class="contact-item">
          <svg width="22" height="18" viewBox="0 0 22 18" aria-hidden="true"><path d="M1 6c0-3 4-5 10-5s10 2 10 5v2h-5V5.5c-1.5-.7-3-.9-5-.9s-3.5.2-5 .9V8H1z"/><path d="M5 9h12l2 8H3z"/></svg>
          913 555 0172
        </span>
        <span class="contact-item">
          <svg width="22" height="16" viewBox="0 0 22 16" aria-hidden="true"><path d="M1 1h20v14H1z M2.5 2.5v.3l8.5 6.5 8.5-6.5v-.3z M2.5 4.8v8.7h17V4.8l-8.5 6.5z" fill-rule="evenodd"/></svg>
          d.fenwick@hapteam.us
        </span>
        <span class="contact-item">
          <svg width="22" height="22" viewBox="0 0 22 22" aria-hidden="true"><circle cx="11" cy="11" r="10"/><path d="M2 11h18M11 1.5c-3 3-3 16 0 19M11 1.5c3 3 3 16 0 19" stroke="#3f5ca3" stroke-width="1.4" fill="none"/></svg>
          www.hapteam.com
        </span>
      </div>
      <div class="contact-row contact-row--address">
        <span class="contact-item">
          <svg width="16" height="22" viewBox="0 0 16 22" aria-hidden="true"><path d="M8 0a8 8 0 0 1 8 8c0 5-8 14-8 14S0 13 0 8a8 8 0 0 1 8-8zm0 4.5a3.5 3.5 0 1 0 0 7 3.5 3.5 0 0 0 0-7z" fill-rule="evenodd"/></svg>
          31842 204th Lane, Leavenworth, KS 66099
        </span>
      </div>
    </div>
  </section>
</body>
</html>
```